Travinex - You are the Boss!

Travinex is a new Silicon Valley company, of the pelim founders from Berlin, which provides a "Shared Pioneer Circle". This platform allows the crowd to support startups with money, experts and fame. Our Vision is, that everyone should become an entrepreneur.

Pls find all brief details in the attached document
Updates

Would be nice to have a list of more social services I'm available on, like a list of pictograms of all my services:

Find me on: vooka, bramlet+, qrt, fenwix, moodrail, zupp, hvoxa, etc...

pls make sure to use the right font:
http://www.typemarlow.com/fonts/Velquin

Target Market(s)

Main target market is those already involved in the startup industry, by fundraising, investing, advising, cofounding and working. Travinex brings a totaly new transparency and collaborative way of starting companies to that business.

· Entrepreneurs (looking for funding, team and community)
· Investors (looking for hot investments and )
· Experts (workers looking for startups they can work for equity)
· Incubators & Business Schools (looking for tools to advise startups)

Industry/Entity Type

It Company

Requirements
Must have
• Pls find all brief details in the attached document
Nice to have

```html
<!DOCTYPE html>
<html lang="en">
<head>
<meta charset="utf-8">
<title>Travinex – Business Card</title>
<link rel="stylesheet" href="https://fonts.googleapis.com/css2?family=Jura:wght@500;700&family=Arimo:wght@400;700&display=swap">
<style>
  :root {
    --stage: #ecebe8;
    --card: #ffffff;
    --charcoal: #434446;
    --orange: #ec6a3f;
    --text-dark: #3c3c3c;
    --logo-grey: #555759;
    --muted: #b9b9b9;
  }
  * { margin: 0; padding: 0; box-sizing: border-box; }
  html, body { width: 1200px; height: 900px; overflow: hidden; }
  body { background: var(--stage); position: relative; font-family: "Jura", sans-serif; }

  .card { position: absolute; background: var(--card); box-shadow: 0 6px 18px rgba(0,0,0,.28); overflow: hidden; }

  /* Front */
  .card-front { left: 70px; top: 52px; width: 654px; height: 368px; }
  .front-panel { position: absolute; inset: 0; }
  .holder { position: absolute; left: 36px; top: 40px; color: #fff; }
  .holder-name { font-weight: 700; font-size: 24px; letter-spacing: .5px; }
  .holder-role { font-weight: 500; font-size: 18px; margin-top: 2px; }
  .contact { position: absolute; left: 26px; top: 204px; color: #fff; font-weight: 500; font-size: 15px; line-height: 28px; }
  .social { list-style: none; margin-top: 6px; }
  .social li { display: flex; align-items: center; gap: 8px; line-height: 26px; }
  .social-mark { width: 15px; height: 15px; border-radius: 2px; background: #6d8cc4; flex: none; }
  .social li:nth-child(2) .social-mark { background: #3d7fb8; }
  .social li:nth-child(3) .social-mark { background: #5bb6e4; }

  .brand { position: absolute; left: 396px; top: 58px; width: 230px; text-align: center; }
  .brand-dot { width: 96px; height: 96px; border-radius: 50%; background: var(--orange); margin: 0 auto 18px; }
  .brand-name { font-family: "Arimo", sans-serif; font-weight: 700; font-size: 38px; color: var(--logo-grey); line-height: 1; }
  .brand-tagline { font-family: "Arimo", sans-serif; font-size: 15px; color: var(--orange); text-align: right; margin-top: 4px; padding-right: 6px; }

  /* Back */
  .card-back { left: 476px; top: 456px; width: 656px; height: 368px; }
  .invite { position: absolute; left: 40px; top: 14px; width: 564px; height: 100px; background: var(--charcoal); border: 5px solid var(--orange); color: #fff; text-align: center; padding-top: 12px; }
  .invite-question { font-weight: 500; font-size: 19px; }
  .invite-cta { font-weight: 700; font-size: 18px; margin-top: 12px; }
  .invite-tail { position: absolute; left: 50px; top: 109px; }
  .company { position: absolute; left: 0; right: 0; top: 120px; text-align: center; color: var(--text-dark); }
  .company-name { font-family: "Arimo", sans-serif; font-weight: 700; font-size: 17px; line-height: 22px; }
  .company-address { font-weight: 500; font-size: 15px; line-height: 20px; }
  .divider { position: absolute; left: 0; right: 0; top: 230px; height: 4px; background: var(--charcoal); }
  .notes-label { position: absolute; right: 18px; top: 240px; color: var(--muted); font-size: 16px; font-weight: 500; }
  .notes-list { position: absolute; left: 48px; top: 256px; list-style: none; color: var(--text-dark); font-weight: 500; font-size: 15px; line-height: 27px; }
</style>
</head>
<body>

<section class="card card-front">
  <svg class="front-panel" width="654" height="368" viewBox="0 0 654 368" aria-hidden="true">
    <path d="M0 0 H456 Q332 184 474 368 H0 Z" fill="none" stroke="var(--orange)" stroke-width="6"/>
    <path d="M0 0 H436 Q310 184 454 368 H0 Z" fill="var(--charcoal)"/>
  </svg>

  <div class="holder">
    <p class="holder-name">Mara Kellten</p>
    <p class="holder-role">Founder and CTO</p>
  </div>

  <div class="contact">
    <p>Mobile: xxx xxx xxxx</p>
    <p>Email: mke@travinex.com</p>
    <ul class="social">
      <li><span class="social-mark"></span>Frendly.com/marakellten</li>
      <li><span class="social-mark"></span>workly.com/in/marakellten</li>
      <li><span class="social-mark"></span>Chirpo.com/marakellten</li>
    </ul>
  </div>

  <div class="brand">
    <div class="brand-dot"></div>
    <p class="brand-name">Travinex</p>
    <p class="brand-tagline">Run the Show Now!</p>
  </div>
</section>

<section class="card card-back">
  <div class="invite">
    <p class="invite-question">Are you interested in Startups, Investments, Work?</p>
    <p class="invite-cta">Join us on - Frendly.com/Travinex</p>
  </div>
  <svg class="invite-tail" width="30" height="22" viewBox="0 0 30 22" aria-hidden="true">
    <path d="M0 0 H26 L4 20 Z" fill="var(--orange)"/>
  </svg>

  <div class="company">
    <p class="company-name">Travinex</p>
    <p class="company-name">Run the Show Now!</p>
    <p class="company-address">Berlin - Lindenhof Platz 14 | 10117 Berlin | Germany</p>
    <p class="company-address">Silicon Valley - 212 Orchard Ave | Sunnyvale | CA 94086</p>
  </div>

  <div class="divider"></div>
  <p class="notes-label">Notes</p>
  <ul class="notes-list">
    <li>date and event of meeting,</li>
    <li>keywords,</li>
    <li>follow-up,</li>
  </ul>
</section>

</body>
</html>
```